Visit card

Industry/Entity Type

Health Care

Contact Information for Business Card

O VITAL SYSTEMIQUE
Odile Ferrand - chef de Projet

Requirements
Must have
• 318 Rue des Tilleuls Verts 47150 MERLONVILLE Tel: 33 (0) 487 204 615 Mobile: 06 42 93 17 58 Web: www.cliniqorvane.example Contact: o.ferrand@o-vitalsystemique.example
Should not have
• Respect for color

```html
<!DOCTYPE html>
<html lang="fr">
<head>
<meta charset="utf-8">
<title>O VITAL SYSTEMIQUE – Carte de visite</title>
<link rel="stylesheet" href="https://fonts.googleapis.com/css2?family=Barlow:wght@400;600&family=Montserrat:wght@600&display=swap">
<style>
  :root {
    --stage: #b3bec1;
    --card: #c2cbcd;
    --card-edge: #e4e9ea;
    --red-bright: #ec1f2b;
    --red-deep: #c01921;
    --ink: #111416;
    --mark-grey: #4a4a4b;
    --white: #ffffff;
  }
  * { margin: 0; padding: 0; box-sizing: border-box; }
  html, body {
    width: 1200px; height: 1000px; overflow: hidden;
    background: var(--stage);
  }
  .card {
    position: absolute; left: 342px; width: 516px; height: 335px;
    background: var(--card);
    border: 1px solid var(--card-edge);
    overflow: hidden;
  }
  .card--front { top: 143px; }
  .card--back { top: 525px; }
  .card-shapes { position: absolute; inset: 0; width: 100%; height: 100%; }

  .brand {
    position: absolute; left: 106px; top: 181px;
    display: flex; align-items: center; gap: 22px;
  }
  .brand-dot {
    width: 112px; height: 112px; border-radius: 50%;
    background: var(--mark-grey); flex: none;
  }
  .brand-name {
    font-family: "Montserrat", sans-serif; font-weight: 600;
    font-size: 28px; line-height: 1.15; letter-spacing: 1px;
    color: var(--mark-grey);
  }

  .brand-small {
    position: absolute; right: 20px; top: 22px;
    display: flex; align-items: center; gap: 8px;
  }
  .brand-small .brand-name { font-size: 11px; color: var(--white); letter-spacing: .5px; }
  .brand-small .brand-dot { width: 34px; height: 34px; background: var(--white); }

  .person { position: absolute; left: 23px; top: 140px; font-family: "Barlow", sans-serif; color: var(--ink); }
  .person-name { font-weight: 600; font-size: 19px; line-height: 1.2; }
  .person-role { font-size: 15px; margin-top: 3px; }

  .contacts {
    position: absolute; left: 22px; top: 210px; list-style: none;
    font-family: "Barlow", sans-serif; font-size: 14px; color: var(--ink);
  }
  .contacts li { display: flex; align-items: center; height: 27px; }
  .contacts li:nth-child(4) { height: 23px; }
  .contacts svg { width: 10px; height: 10px; margin-right: 9px; fill: var(--ink); flex: none; }
</style>
</head>
<body>

<section class="card card--front">
  <svg class="card-shapes" viewBox="0 0 516 335" preserveAspectRatio="none" aria-hidden="true">
    <path d="M0,0 H516 V122 C380,82 90,110 0,335 Z" fill="var(--red-deep)"/>
    <path d="M0,0 H516 V122 Z" fill="var(--red-bright)"/>
  </svg>
  <div class="brand">
    <span class="brand-dot"></span>
    <span class="brand-name">O VITAL<br>SYSTEMIQUE</span>
  </div>
</section>

<section class="card card--back">
  <svg class="card-shapes" viewBox="0 0 516 335" preserveAspectRatio="none" aria-hidden="true">
    <path d="M0,122 L516,0 V335 C470,190 320,95 90,116 Z" fill="var(--red-deep)"/>
    <path d="M0,0 H516 L0,122 Z" fill="var(--red-bright)"/>
  </svg>
  <div class="brand-small">
    <span class="brand-name">O VITAL SYSTEMIQUE</span>
    <span class="brand-dot"></span>
  </div>
  <div class="person">
    <p class="person-name">Odile Ferrand</p>
    <p class="person-role">chef de Projet</p>
  </div>
  <ul class="contacts">
    <li><svg viewBox="0 0 10 10"><path d="M5,0 A3.6,3.6 0 0 1 8.6,3.6 C8.6,6 5,10 5,10 C5,10 1.4,6 1.4,3.6 A3.6,3.6 0 0 1 5,0 Z M5,2.3 A1.3,1.3 0 1 0 5,4.9 A1.3,1.3 0 1 0 5,2.3 Z"/></svg>318 Rue des Tilleuls Verts 47150 Merlonville</li>
    <li><svg viewBox="0 0 10 10"><path d="M2,0.5 L3.8,0.5 L4.4,3 L3.2,4 C3.8,5.4 4.6,6.2 6,6.8 L7,5.6 L9.5,6.2 L9.5,8 C9.5,9 8.6,9.6 7.6,9.4 C4,8.6 1.4,6 0.6,2.4 C0.4,1.4 1,0.5 2,0.5 Z"/></svg>+33 (0) 487 204 615 / 06 42 93 17 58</li>
    <li><svg viewBox="0 0 10 10"><circle cx="5" cy="5" r="4.3" fill="none" stroke="var(--ink)" stroke-width="1.1"/><path d="M0.7,5 H9.3 M5,0.7 C2.6,3 2.6,7 5,9.3 M5,0.7 C7.4,3 7.4,7 5,9.3" fill="none" stroke="var(--ink)" stroke-width="0.9"/></svg>www.cliniqorvane.example</li>
    <li><svg viewBox="0 0 10 10"><path d="M0.5,2 H9.5 V8.5 H0.5 Z"/><path d="M0.8,2.3 L5,5.6 L9.2,2.3" fill="none" stroke="var(--card)" stroke-width="0.9"/></svg>o.ferrand@o-vitalsystemique.example</li>
  </ul>
</section>

</body>
</html>
```